Harbor Networks Pty Ltd

We are a Sydney based IT services company, providing managed services for corporate clients, established for over 10 years. Amongst our services we provide full infrastructure support, maintenance and upgrades. We also provide helpdesk/remote support and cloud services.

We were hoping to keep our original colours and our logo (Blue and Green, please visit our website www.harbornetworks-demo.com.au) however we are looking for a new business card design (with better resolution and finish) with multiple variation of the blue and green colour design options. Happy for alternative suggestion. ie new blue and green / grey and green / blue and grey et and please feel free to update current logo size ie large or smaller. (Attached our current logo and business card desig)

Business

Contact Information for Business Card

Name, Title, Address, Contract Information, Company Name and Logo.
(QR code if possible)

Colors
0455a3
33a6d7
3276b5
85acd3
85cae6
9bcb3c
add136
cadf82
e9f1ce

```html
<!DOCTYPE html>
<html lang="en">
<head>
<meta charset="utf-8">
<title>Harbor Networks – Business Card</title>
<link href="https://fonts.googleapis.com/css2?family=Open+Sans:wght@300;400;600;700&display=swap" rel="stylesheet">
<style>
  :root {
    --backdrop: #d9d9d9;
    --paper: #ffffff;
    --blue-deep: #0455a3;
    --blue-mid: #3276b5;
    --green-main: #9bcb3c;
    --green-bright: #add136;
    --green-soft: #cadf82;
    --green-pale: #e9f1ce;
    --ink: #333333;
    --ink-soft: #555555;
  }
  * { box-sizing: border-box; margin: 0; padding: 0; }
  html, body { width: 1200px; height: 1023px; overflow: hidden; }
  body {
    background: var(--backdrop);
    font-family: "Open Sans", Arial, sans-serif;
    color: var(--ink);
    position: relative;
  }
  .card {
    position: absolute;
    width: 620px;
    height: 354px;
    border-radius: 4px;
    overflow: hidden;
    box-shadow: 0 10px 24px rgba(0,0,0,0.25);
  }
  .card-front { left: 90px; top: 110px; background: var(--paper); }
  .card-back {
    left: 490px; top: 560px;
    background: linear-gradient(135deg, var(--green-soft) 0%, var(--green-bright) 45%, var(--green-main) 100%);
  }

  /* front */
  .front-head { position: absolute; left: 0; top: 0; width: 100%; height: 200px; }
  .company-name {
    position: absolute;
    font-weight: 600;
    white-space: nowrap;
  }
  .front-head .company-name {
    left: 42px; top: 74px;
    font-size: 38px; letter-spacing: -0.5px; color: var(--blue-deep);
  }
  .person { position: absolute; left: 42px; top: 138px; }
  .person-name { font-size: 20px; font-weight: 700; color: var(--blue-mid); }
  .person-title { font-size: 13px; color: var(--ink-soft); margin-top: 2px; }
  .person-title .divider { color: var(--green-main); padding: 0 4px; }
  .rule {
    position: absolute; left: 0; top: 200px; width: 100%; height: 2px; background: var(--blue-mid);
  }
  .front-band {
    position: absolute; left: 0; top: 202px; width: 100%; height: 152px;
    background: linear-gradient(120deg, var(--green-pale) 0%, var(--green-soft) 30%, var(--green-bright) 70%, var(--green-main) 100%);
  }
  .contacts {
    position: absolute; left: 42px; top: 16px;
    display: grid; grid-template-columns: 86px auto; row-gap: 1px;
    font-size: 12.5px; line-height: 18px;
  }
  .contacts dt { color: var(--ink-soft); }
  .contacts dt .initial { color: var(--blue-mid); font-weight: 600; }
  .contacts dd { color: var(--ink); white-space: nowrap; }
  .address {
    position: absolute; right: 30px; top: 16px; text-align: right;
    font-size: 12.5px; line-height: 18px; color: var(--ink); font-style: normal;
  }
  .address .company { color: var(--blue-mid); font-weight: 700; }

  /* back */
  .card-back .company-name {
    left: 0; right: 0; top: 148px; text-align: center;
    color: var(--paper); font-weight: 300; font-size: 52px;
  }
</style>
</head>
<body>

<section class="card card-front" aria-label="Business card front">
  <div class="front-head">
    <div class="company-name">Harbor Networks</div>
    <div class="person">
      <div class="person-name">Dana Mercer</div>
      <div class="person-title">Director<span class="divider">|</span>Managed IT Services</div>
    </div>
  </div>
  <div class="rule"></div>
  <div class="front-band">
    <dl class="contacts">
      <dt><span class="initial">T</span>el:</dt><dd>1300 555 010</dd>
      <dt><span class="initial">D</span>irect:</dt><dd>+61 2 5550 1234</dd>
      <dt><span class="initial">F</span>ax:</dt><dd>+61 2 5550 5678</dd>
      <dt><span class="initial">M</span>ob:</dt><dd>+61 400 555 019</dd>
      <dt><span class="initial">H</span>elpdesk:</dt><dd>support@harbornetworks-demo.com.au</dd>
      <dt><span class="initial">E</span>mail:</dt><dd>dana.mercer@harbornetworks-demo.com.au</dd>
    </dl>
    <address class="address">
      <div class="company">Harbor Networks Pty Ltd</div>
      <div>Level 4, 118 Wharf Lane</div>
      <div>Sydney NSW 2000 Australia</div>
      <div>www.harbornetworks-demo.com.au</div>
    </address>
  </div>
</section>

<section class="card card-back" aria-label="Business card back">
  <div class="company-name">Harbor Networks</div>
</section>

</body>
</html>
```